依頼詳細
ゴミ屋敷の片づけ・遺品整理等の事業になります。
ポスティングを想定しています。
ターゲットは高齢者になりますのでわかりやすいデザインでお願いします。
記載項目
屋号:そよかぜクリーンサービス
電話番号:未定
サイズ
A4
ページ数
両面
希望イメージ
シンプル 複雑
単色 カラフル
暗い 明るい
日常 高級
遊び心 厳粛
未来的 伝統的
女性的 男性的
希望する色
緑系
納品ファイル
• 高解像度JPG (.jpg)
補足説明
■ 選んだ理由

高齢者向けということでイラストを多用しわかりやすいデザインで気に入りました。
ベースもやさしめの色合いで好きです。

■ 提案者全員のお礼・コメント

さまざまな提案をいただき感謝しています。ありがとうございました。

```html
<!DOCTYPE html>
<html lang="ja">
<head>
<meta charset="utf-8">
<title>そよかぜクリーンサービス チラシ</title>
<link href="https://fonts.googleapis.com/css2?family=M+PLUS+Rounded+1c:wght@400;700;800;900&display=swap" rel="stylesheet">
<style>
:root{
  --green:#3f9a2e;
  --green-dark:#24701c;
  --green-light:#e6f3d4;
  --green-pale:#f3f9ea;
  --red:#e3342a;
  --yellow:#ffe100;
  --ink:#333;
  --white:#fff;
  --illust-a:#cfe4b8;
  --illust-b:#f3e2c4;
}
*{box-sizing:border-box;margin:0;padding:0}
html,body{width:855px;height:1200px;overflow:hidden}
body{font-family:"M PLUS Rounded 1c",sans-serif;color:var(--ink);background:var(--white)}
.flyer{position:relative;width:855px;height:1200px;background:linear-gradient(180deg,var(--green-pale) 0%,var(--green-light) 100%);overflow:hidden}

/* header */
.header{position:absolute;left:0;top:0;width:855px;height:248px}
.tag-save{position:absolute;left:0;top:12px;background:var(--red);color:var(--white);font-weight:900;font-size:22px;padding:6px 12px;border-radius:0 8px 8px 0}
.catch{position:absolute;left:190px;top:8px;width:540px;height:46px;background:var(--green);color:var(--white);font-weight:800;font-size:26px;line-height:46px;text-align:center;border-radius:23px}
.leave-it{position:absolute;left:26px;top:82px;color:var(--red);font-weight:900;font-size:28px;transform:rotate(-8deg)}
.dutch-label{position:absolute;left:250px;top:68px;background:var(--green-dark);color:var(--yellow);font-weight:900;font-size:38px;padding:2px 26px;border-radius:10px;letter-spacing:4px}
.brand{position:absolute;left:22px;top:138px;font-weight:900;font-size:66px;line-height:1.2;letter-spacing:-1px;color:var(--green);white-space:nowrap}
.brand .soft{color:var(--green-dark)}
.hero-illust{position:absolute;right:12px;top:8px;width:90px;height:118px;border-radius:12px;background:linear-gradient(180deg,var(--illust-a),var(--illust-b))}

/* service panels */
.services{position:absolute;left:14px;top:248px;width:827px;display:grid;grid-template-columns:1fr 1fr;grid-template-rows:220px 232px 224px;gap:10px 13px}
.panel{position:relative;background:var(--white);border:3px solid var(--green);border-radius:14px;padding:10px 14px;overflow:hidden}
.panel h2{font-weight:900;font-size:30px;color:var(--green-dark);line-height:1.15;margin-bottom:8px}
.panel .body{font-weight:700;font-size:15px;line-height:1.55}
.panel ul{list-style:none}
.panel .illust{position:absolute;border-radius:10px;background:linear-gradient(135deg,var(--illust-a),var(--illust-b))}
.p1 ul{width:215px;font-size:16px}
.p1 .illust{right:12px;top:58px;width:160px;height:146px}
.p2 .body{width:225px}
.p2 .illust{right:12px;top:58px;width:140px;height:150px}
.p3 .illust{left:12px;top:96px;width:104px;height:112px}
.p3 ul{margin-left:116px}
.p4 .body{width:245px}
.p4 .illust{right:12px;top:58px;width:114px;height:156px}
.p5 .illust{left:14px;top:58px;width:370px;height:60px}
.p5 .body{margin-top:74px}
.p6 .body{width:245px}
.p6 .illust{right:12px;top:56px;width:116px;height:156px}

/* slogan band */
.slogan{position:absolute;left:14px;top:952px;width:827px;height:46px;background:var(--green);color:var(--white);font-weight:900;font-size:32px;line-height:46px;text-align:center;border-radius:23px}

/* contact */
.contact{position:absolute;left:0;top:1004px;width:855px;height:196px}
.contact-illust{position:absolute;left:14px;top:0;width:80px;height:90px;border-radius:10px;background:linear-gradient(180deg,var(--illust-a),var(--illust-b))}
.contact-illust.right{left:auto;right:14px;width:90px;height:84px}
.contact-note{position:absolute;left:104px;top:2px;width:580px;font-weight:800;font-size:18px;line-height:1.3;color:var(--green-dark)}
.badge{position:absolute;right:112px;top:52px;background:var(--white);border:3px solid var(--green);color:var(--green-dark);font-weight:900;font-size:19px;padding:2px 12px;border-radius:8px}
.footer-bar{position:absolute;left:0;top:96px;width:855px;height:100px;background:var(--white);border-top:4px solid var(--green)}
.footer-brand{position:absolute;left:100px;top:2px;font-weight:900;font-size:40px;line-height:1.15;color:var(--green)}
.phone{position:absolute;left:14px;top:50px;display:flex;align-items:center;gap:8px;font-weight:900;font-size:40px;line-height:1.1;color:var(--green-dark);letter-spacing:1px}
.phone svg{width:36px;height:36px}
.info{position:absolute;left:520px;top:48px;width:330px;font-weight:700;font-size:11px;line-height:1.45}
</style>
</head>
<body>
<div class="flyer">
  <header class="header">
    <div class="tag-save">完全保存版！</div>
    <div class="catch">暮らしの困った！に、必ず役にたちます！</div>
    <div class="leave-it">お任せください！</div>
    <div class="dutch-label">断捨離請負人</div>
    <h1 class="brand"><span class="soft">そよかぜ</span>クリーンサービス</h1>
    <div class="hero-illust" role="img" aria-label="作業着姿のスタッフのイラスト"></div>
  </header>

  <main class="services">
    <section class="panel p1">
      <h2>〜暮らしのお片付け〜</h2>
      <ul class="body">
        <li>・ゴミ屋敷をピカピカに！</li>
        <li>・ベランダのお掃除！</li>
        <li>・不用品の処分！</li>
      </ul>
      <div class="illust" role="img" aria-label="片付けた部屋とゴミ袋のイラスト"></div>
    </section>
    <section class="panel p2">
      <h2>〜遺品の整理〜</h2>
      <p class="body">思い出が詰まった大切な遺品。当社が丁寧に整理致します。その他遺品に関するお悩みご相談承ります。</p>
      <div class="illust" role="img" aria-label="遺品整理の相談をする家族のイラスト"></div>
    </section>
    <section class="panel p3">
      <h2>〜トランクルームの<br>　お片付け〜</h2>
      <ul class="body">
        <li>・お荷物を整理の場所まで、丁寧にお運びします！</li>
        <li>・もちろん不用品処分も致します！</li>
      </ul>
      <div class="illust" role="img" aria-label="荷物を運ぶスタッフのイラスト"></div>
    </section>
    <section class="panel p4">
      <h2>〜リフォーム〜</h2>
      <p class="body">遺品整理後の壁紙修繕から床の張替・エアコン取付けなど！小さなことから大きなことまでご相談下さい！</p>
      <div class="illust" role="img" aria-label="リフォーム作業をする職人のイラスト"></div>
    </section>
    <section class="panel p5">
      <h2>〜電気の困った〜</h2>
      <div class="illust" role="img" aria-label="エアコンのイラスト"></div>
      <p class="body">エアコンの取外しやウォシュレットの交換など、電気の困ったもご相談ください！</p>
    </section>
    <section class="panel p6">
      <h2>〜高価買取〜</h2>
      <p class="body">ただ処分するだけではありません！まだ使える家具・貴金属等高価買取致します！この機会にご相談ください！</p>
      <div class="illust" role="img" aria-label="壺や家具など買取品のイラスト"></div>
    </section>
  </main>

  <div class="slogan">お部屋をキレイに！毎日を快適に！</div>

  <footer class="contact">
    <div class="contact-illust" role="img" aria-label="電話を受けるスタッフのイラスト"></div>
    <p class="contact-note">まずはお電話でお見積りを！よろしければその日の作業も可能！<br>どんなことでもお気軽に御相談下さい。<br>お電話お待ちしております。</p>
    <div class="badge">電話見積り・即日対応可能</div>
    <div class="contact-illust right" role="img" aria-label="お辞儀するスタッフのイラスト"></div>
    <div class="footer-bar">
      <div class="footer-brand">そよかぜクリーンサービス</div>
      <div class="phone">
        <svg viewBox="0 0 24 24" aria-hidden="true"><path fill="#24701c" d="M6.6 10.8c1.4 2.8 3.8 5.1 6.6 6.6l2.2-2.2c.3-.3.7-.4 1-.2 1.1.4 2.3.6 3.6.6.6 0 1 .4 1 1V20c0 .6-.4 1-1 1C10.6 21 3 13.4 3 4c0-.6.4-1 1-1h3.5c.6 0 1 .4 1 1 0 1.3.2 2.5.6 3.6.1.3 0 .7-.2 1z"/></svg>
        03-4820-7315
      </div>
      <p class="info">各種クレジットカードOK！<br>東京都緑ヶ丘区みどり町 2-8-5　(株)みどりの手<br>営業時間 AM9:00〜PM8:00　定休日 日祝日</p>
    </div>
  </footer>
</div>
</body>
</html>
```